Eye catchy Construction Development business cards and stationery
Torvane Arch
Modern
Your Name
Managing Director
11111 My Street suite #100 City, STATE 66211
myemail@email.com
www.mywebsite.com
Use my winning logo from here http://www.plumvexstudio.com/contests/logo-for-construction-developer-company
Some elegant but modern design. One idea would be to use the company logo printed on silver metallic look, such as http://www.plumvexstudio.com/contests/theoakhearth-logo-project

```html
<!DOCTYPE html>
<html lang="en">
<head>
<meta charset="utf-8">
<title>Torvane Arch – Business Cards</title>
<link rel="stylesheet" href="https://fonts.googleapis.com/css2?family=Montserrat:wght@400;500;600;700&display=swap">
<style>
  :root {
    --teal: #1c7fa8;
    --orange: #f39a1e;
    --ink: #3d4a52;
    --paper: #ffffff;
    --ground: #e4e6e8;
  }
  * { margin: 0; padding: 0; box-sizing: border-box; }
  html, body {
    width: 1200px; height: 895px; overflow: hidden;
    background: var(--ground);
    font-family: "Montserrat", sans-serif;
    color: var(--ink);
  }
  .stage { position: relative; width: 1200px; height: 895px; }
  .card {
    position: absolute; left: 270px;
    width: 660px; height: 377px;
    background: var(--paper);
    box-shadow: 0 3px 12px rgba(0,0,0,.12);
    overflow: hidden;
  }
  .card--front { top: 50px; }
  .card--back { top: 468px; }

  /* Brand lockup */
  .brand { position: absolute; display: flex; align-items: center; }
  .brand__dot { border-radius: 50%; background: var(--teal); flex: none; }
  .brand__name { color: var(--teal); font-weight: 600; line-height: 1; letter-spacing: .5px; }
  .brand__tag { color: var(--orange); font-weight: 500; letter-spacing: 1px; margin-top: 4px; }

  .card--front .brand { left: 118px; top: 138px; }
  .card--front .brand__dot { width: 96px; height: 96px; margin-right: 22px; }
  .card--front .brand__name { font-size: 44px; }
  .card--front .brand__tag { font-size: 15px; }

  .card--back .brand { left: 22px; top: 22px; }
  .card--back .brand__dot { width: 40px; height: 40px; margin-right: 10px; }
  .card--back .brand__name { font-size: 24px; }
  .card--back .brand__tag { font-size: 10px; margin-top: 3px; }

  /* Back layout */
  .accent-block { position: absolute; left: 0; top: 126px; width: 178px; height: 42px; background: var(--orange); }
  .web-band {
    position: absolute; left: 178px; top: 168px; width: 482px; height: 44px;
    background: var(--teal); color: #fff;
    font-size: 13px; font-weight: 500; letter-spacing: .5px;
    display: flex; align-items: center; padding-left: 26px;
  }
  .person { position: absolute; left: 446px; top: 126px; }
  .person__name { font-size: 16px; font-weight: 600; color: var(--teal); letter-spacing: 1px; }
  .person__role { font-size: 10px; font-weight: 500; color: var(--ink); letter-spacing: 1px; margin-top: 2px; text-transform: uppercase; }

  .contact { position: absolute; left: 26px; top: 182px; list-style: none; }
  .contact li, .links li { display: flex; align-items: center; font-size: 10px; height: 20px; }
  .icon {
    width: 13px; height: 13px; margin-right: 8px; background: var(--teal);
    display: flex; align-items: center; justify-content: center; flex: none;
  }
  .links { position: absolute; left: 386px; top: 268px; list-style: none; }
  .links li { height: 22px; }
  .links .icon { width: 14px; height: 14px; }
</style>
</head>
<body>
<main class="stage">
  <section class="card card--front" aria-label="Card front">
    <div class="brand">
      <span class="brand__dot"></span>
      <div>
        <div class="brand__name">Torvane Arch</div>
        <div class="brand__tag">DESIGN &amp; CONSTRUCTION</div>
      </div>
    </div>
  </section>

  <section class="card card--back" aria-label="Card back">
    <div class="brand">
      <span class="brand__dot"></span>
      <div>
        <div class="brand__name">Torvane Arch</div>
        <div class="brand__tag">DESIGN &amp; CONSTRUCTION</div>
      </div>
    </div>

    <div class="accent-block"></div>
    <div class="web-band">www.torvanearch.com/123</div>

    <div class="person">
      <div class="person__name">DANA WHITLOW</div>
      <div class="person__role">Managing Director</div>
    </div>

    <ul class="contact">
      <li><span class="icon"><svg width="9" height="9" viewBox="0 0 10 10"><path d="M5 0.5a3 3 0 0 1 3 3c0 2.3-3 6-3 6s-3-3.7-3-6a3 3 0 0 1 3-3z" fill="#fff"/></svg></span>Harbor Lane 48</li>
      <li><span class="icon"><svg width="9" height="9" viewBox="0 0 10 10"><path d="M2 1h2l1 2.5-1.2 1a5 5 0 0 0 2 2l1-1.2L9 6.3v2A1 1 0 0 1 8 9.3 7.5 7.5 0 0 1 1 2a1 1 0 0 1 1-1z" fill="#fff"/></svg></span>014 552 0193</li>
      <li><span class="icon"><svg width="9" height="9" viewBox="0 0 10 10"><rect x="1" y="2.5" width="8" height="5.5" fill="none" stroke="#fff" stroke-width="1"/><path d="M1 2.5l4 3 4-3" fill="none" stroke="#fff" stroke-width="1"/></svg></span>hello@torvanearch.com</li>
    </ul>

    <ul class="links">
      <li><span class="icon"></span>www.torvanearch.com</li>
      <li><span class="icon"></span>studio.torvane.net</li>
      <li><span class="icon"></span>news.torvane.net</li>
    </ul>
  </section>
</main>
</body>
</html>
```